Astrology Web Site in Need of a Clean & Modern Design

Over the past few months we've converted our site to Wordpress. With the content and structure now in place, it's time for a clean, modern design. Our new site must engage visitors, delivering insights and guidance through a well designed UI/UX. We're taking online astrology to the next level! We've sourced hundreds of amazing images and with the eye of a talented designer we can achieve our goals. Our Wordpress developer is ready to convert your design and launch a truly showcase site. Attached are a few examples of what we would like the design to be modeled on. Further details are included in the attached document "Templates to Design for StarlitPathway.com"

Target Market(s)

female

Industry/Entity Type

Online

Number of Pages Required

4 page

Requirements
Must have
• Use real images and not illustrations.
• Use a 12-columns grid system.
• Zodiac signs/icons should be of a single color with no gradients.
Should not have
• crystals balls, fortune tellers etc...dark and heavy backgrounds (ignore current site design and color).

```html
<!DOCTYPE html>
<html lang="en">
<head>
<meta charset="utf-8">
<title>Starlit Astrology</title>
<link href="https://fonts.googleapis.com/css2?family=Montserrat:wght@400;500;600;700&family=Roboto:wght@400;500&family=Open+Sans:wght@400;600&display=swap" rel="stylesheet">
<style>
:root{
  --ink:#1b1b1b;
  --header:#161616;
  --footer:#121212;
  --footer-base:#0a0a0a;
  --purple:#8a1a8a;
  --purple-deep:#7a167a;
  --blue:#1a9fd6;
  --band:#e6e6e6;
  --panel:#d3d3d3;
  --text:#555;
  --muted:#8a8a8a;
  --white:#fff;
  --input:#ecd3ec;
}
*{margin:0;padding:0;box-sizing:border-box}
html,body{width:736px;height:1200px;overflow:hidden;background:var(--white)}
body{font-family:"Open Sans",Arial,sans-serif;color:var(--text);position:relative}
.abs{position:absolute}
.site-header{left:0;top:0;width:736px;height:56px;background:var(--header)}
.brand{left:68px;top:19px;font-family:"Montserrat",sans-serif;font-weight:700;font-size:14px;color:var(--white);letter-spacing:.4px}
.main-nav{top:0;left:0;width:736px;height:56px;list-style:none}
.main-nav li{position:absolute;top:25px;font-family:"Montserrat",sans-serif;font-size:7px;font-weight:500;color:var(--white);letter-spacing:.2px}
.main-nav li.active{color:var(--blue)}
.hero{left:0;top:56px;width:736px;height:304px;background:radial-gradient(ellipse at 38% 45%,#8a7a55 0%,#4a3a22 30%,#1a120a 65%,#080604 100%)}
.hero-caption{left:0;top:296px;width:736px;height:64px;background:rgba(20,14,10,.55)}
.hero-caption p{position:absolute;left:0;top:14px;width:736px;text-align:center;font-family:"Montserrat",sans-serif;font-size:13px;line-height:19px;color:var(--white);letter-spacing:.2px}
.hero-arrow{top:319px;width:22px;height:22px}
.feature-img{top:382px;width:186px;height:112px;border:3px solid var(--white);box-shadow:0 6px 6px -3px rgba(0,0,0,.35)}
.feature h2{position:absolute;top:509px;font-family:"Montserrat",sans-serif;font-weight:500;font-size:13.5px;color:var(--purple)}
.feature p{position:absolute;top:529px;width:192px;font-size:6.6px;line-height:12.6px;color:var(--text)}
.feature a{position:absolute;top:571px;font-family:"Montserrat",sans-serif;font-weight:500;font-size:7px;color:var(--blue);text-decoration:none}
.about{left:0;top:594px;width:736px;height:104px;background:var(--band)}
.section-title{width:736px;left:0;text-align:center;font-family:"Montserrat",sans-serif;font-weight:500;color:var(--ink)}
.section-copy{left:72px;width:592px;text-align:center;font-size:6.8px;line-height:13.6px;color:var(--text)}
.zodiac{top:797px;width:102px;height:86px;text-align:center}
.zodiac .sign-icon{position:absolute;left:29px;top:9px;width:44px;height:44px;border-radius:50%;background:var(--ink)}
.sign-icon svg{display:block;width:44px;height:44px}
.sign-icon path,.sign-icon circle{fill:none;stroke:var(--white);stroke-width:2;stroke-linecap:round;stroke-linejoin:round}
.zodiac span{position:absolute;left:0;top:60px;width:102px;font-family:"Roboto",sans-serif;font-size:9px;color:var(--ink)}
.zodiac.selected{background:var(--ink)}
.zodiac.selected .sign-icon{background:var(--blue)}
.zodiac.selected span{color:var(--white)}
.zodiac-divider{top:797px;width:2px;height:86px;background:linear-gradient(#fff,#ececec,#fff)}
.strip-arrow{top:828px;width:14px;height:14px}
.reading{left:0;top:883px;width:736px;height:155px;background:var(--band)}
.tab{top:902px;height:24px;width:80px;background:var(--ink);color:var(--white);font-family:"Montserrat",sans-serif;font-size:7px;text-align:center;line-height:24px}
.tab.current{background:var(--purple)}
.reading-date{left:68px;top:942px;font-family:"Roboto",sans-serif;font-size:7px;color:var(--blue)}
.reading-text{left:68px;top:955px;width:436px;font-size:6.6px;line-height:13.6px;color:var(--text)}
.stats{left:530px;top:902px;width:137px;height:118px;background:var(--panel);padding:9px 12px}
.stats h4{font-family:"Montserrat",sans-serif;font-weight:500;font-size:6.8px;color:var(--purple);margin-bottom:1px}
.stats p{font-size:6.2px;color:var(--muted);margin-bottom:8px}
.stars{display:block;margin:2px 0 6px}
.site-footer{left:0;top:1038px;width:736px;height:128px;background:var(--footer)}
.footer-base{left:0;top:1166px;width:736px;height:34px;background:var(--footer-base);text-align:center;font-size:6.2px;line-height:34px;color:#4a4a4a}
.footer-title{top:1053px;font-family:"Montserrat",sans-serif;font-weight:500;font-size:9.5px;color:var(--white)}
.post-thumb{left:68px;width:46px;height:32px;background:linear-gradient(135deg,#123a8a,#3a7ad6 50%,#1a2a6a)}
.post-title{left:118px;font-family:"Roboto",sans-serif;font-weight:400;font-size:7px;color:var(--white)}
.post-excerpt{left:118px;width:76px;font-size:6.2px;line-height:10.6px;color:var(--muted)}
.quick-links{list-style:none}
.quick-links li{font-size:6.4px;color:var(--muted);height:15.8px}
.social{list-style:none;left:424px;top:1071px}
.social li{font-size:6.4px;color:var(--muted);height:15.8px;display:flex;align-items:flex-start;gap:5px}
.social i{display:inline-block;width:7px;height:7px;margin-top:1px}
.field{left:529px;width:137px;height:22px;background:var(--input);font-size:6.4px;color:#555;line-height:22px;padding-left:10px}
.subscribe{left:529px;top:1129px;width:137px;height:23px;background:var(--purple-deep);color:var(--white);font-family:"Montserrat",sans-serif;font-weight:600;font-size:7px;text-align:center;line-height:23px}
</style>
</head>
<body>

<header class="site-header abs">
  <div class="brand abs">Starlit Astrology</div>
  <ul class="main-nav abs">
    <li class="active" style="left:242px">HOME</li>
    <li style="left:293px">ABOUT US</li>
    <li style="left:355px">ASTROLOGY</li>
    <li style="left:423px">HOROSCOPES</li>
    <li style="left:499px">COMPATIBILITY</li>
    <li style="left:578px">BLOG</li>
    <li style="left:623px">CONTACT US</li>
  </ul>
</header>

<section class="hero abs" role="img" aria-label="Photo of three lit tea candles in a brass dish on an astrological chart"></section>
<div class="hero-caption abs"><p>UT WISI ENIM AD MINIM VENIAM, QUIS NOSTRUD EXERCI TATION<br>ULLAMCORPER SUSCIPIT LOBORTIS</p></div>
<svg class="hero-arrow abs" style="left:68px" viewBox="0 0 22 22"><circle cx="11" cy="11" r="10" fill="none" stroke="#bbb" stroke-width="1.5"/><path d="M13 6l-5 5 5 5M8 11h8" fill="none" stroke="#bbb" stroke-width="1.5"/></svg>
<svg class="hero-arrow abs" style="left:645px" viewBox="0 0 22 22"><circle cx="11" cy="11" r="10" fill="none" stroke="#bbb" stroke-width="1.5"/><path d="M9 6l5 5-5 5M14 11H6" fill="none" stroke="#bbb" stroke-width="1.5"/></svg>

<article class="feature">
  <div class="feature-img abs" style="left:68px;background:linear-gradient(135deg,#3a1e0c,#9a5a24 50%,#2a160a)" role="img" aria-label="Photo of a glass candle holder on a zodiac wheel"></div>
  <h2 style="left:68px">ASTROLOGY</h2>
  <p style="left:68px">Lorem ipsum dolor sit amet, consectetuer adipiscing elit, sed diam nonummy nibh euismod tincidunt ut laoreet dolore magna aliquam erat volutpat.</p>
  <a style="left:69px">READ MORE</a>
</article>
<article class="feature">
  <div class="feature-img abs" style="left:273px;background:linear-gradient(90deg,#2a0a3a,#b02ac0 40%,#5a1a8a 70%,#1a0a2a)" role="img" aria-label="Image of a zodiac chart panel over a purple light burst"></div>
  <h2 style="left:273px">HOROSCOPES</h2>
  <p style="left:273px">Lorem ipsum dolor sit amet, consectetuer adipiscing elit, sed diam nonummy nibh euismod tincidunt ut laoreet dolore magna aliquam erat volutpat.</p>
  <a style="left:274px">READ MORE</a>
</article>
<article class="feature">
  <div class="feature-img abs" style="left:478px;background:linear-gradient(135deg,#1a2a3a,#6a8aa8 55%,#2a3a4a)" role="img" aria-label="Photo of a hand placing a red puzzle piece"></div>
  <h2 style="left:478px">COMPATIBILITY</h2>
  <p style="left:478px">Lorem ipsum dolor sit amet, consectetuer adipiscing elit, sed diam nonummy nibh euismod tincidunt ut laoreet dolore magna aliquam erat volutpat.</p>
  <a style="left:479px">READ MORE</a>
</article>

<section class="about abs"></section>
<h2 class="section-title abs" style="top:612px;font-size:16px">ABOUT STARLIT ASTROLOGY</h2>
<p class="section-copy abs" style="top:636px">Duis autem vel eum iriure dolor in hendrerit in vulputate velit esse molestie consequat, vel illum dolore eu feugiat nulla facilisis at vero eros et accumsan et iusto odio dignissim qui blandit praesent luptatum zzril delenit augue duis dolore te feugait nulla facilisi. Nam liber tempor cum soluta nobis eleifend option congue nihil imperdiet doming id quod mazim placerat facer possim assum.</p>

<h2 class="section-title abs" style="top:720px;font-size:13px">YOUR DAILY HOROSCOPE LEARN NOW</h2>
<p class="section-copy abs" style="top:742px">Duis autem vel eum iriure dolor in hendrerit in vulputate velit esse molestie consequat, vel illum dolore eu feugiat nulla facilisis at vero eros et accumsan et iusto odio dignissim qui blandit praesent luptatum zzril delenit augue duis dolore te feugait nulla facilisi. Nam liber tempor cum soluta nobis eleifend option congue nihil imperdiet doming id quod mazim placerat facer possim assum.</p>

<svg class="strip-arrow abs" style="left:41px" viewBox="0 0 14 14"><circle cx="7" cy="7" r="6.3" fill="#f3f3f3" stroke="#999"/><path d="M8 4L5 7l3 3" fill="none" stroke="#333" stroke-width="1.4"/></svg>
<svg class="strip-arrow abs" style="left:680px" viewBox="0 0 14 14"><circle cx="7" cy="7" r="6.3" fill="#f3f3f3" stroke="#999"/><path d="M6 4l3 3-3 3" fill="none" stroke="#333" stroke-width="1.4"/></svg>

<div class="zodiac abs" style="left:62px">
  <div class="sign-icon" role="img" aria-label="Pisces sign"><svg viewBox="0 0 44 44"><path d="M14 12Q20 22 14 32M30 12Q24 22 30 32M15 22H29"/></svg></div>
  <span>PISCES</span>
</div>
<div class="zodiac-divider abs" style="left:163px"></div>
<div class="zodiac abs" style="left:164px">
  <div class="sign-icon" role="img" aria-label="Aries sign"><svg viewBox="0 0 44 44"><path d="M22 32V20M22 20Q20 12 15 13Q11 15 14 20M22 20Q24 12 29 13Q33 15 30 20"/></svg></div>
  <span>ARIES</span>
</div>
<div class="zodiac-divider abs" style="left:265px"></div>
<div class="zodiac abs" style="left:266px">
  <div class="sign-icon" role="img" aria-label="Taurus sign"><svg viewBox="0 0 44 44"><circle cx="22" cy="26" r="6"/><path d="M13 13Q16 20 22 20Q28 20 31 13"/></svg></div>
  <span>TAURUS</span>
</div>
<div class="zodiac selected abs" style="left:368px">
  <div class="sign-icon" role="img" aria-label="Gemini sign"><svg viewBox="0 0 44 44"><path d="M14 13Q22 17 30 13M14 31Q22 27 30 31M18 15.5V28.5M26 15.5V28.5"/></svg></div>
  <span>GEMINI</span>
</div>
<div class="zodiac abs" style="left:471px">
  <div class="sign-icon" role="img" aria-label="Cancer sign"><svg viewBox="0 0 44 44"><circle cx="17" cy="19" r="3"/><circle cx="27" cy="25" r="3"/><path d="M17 16Q26 13 32 17M27 28Q18 31 12 27"/></svg></div>
  <span>CANCER</span>
</div>
<div class="zodiac-divider abs" style="left:572px"></div>
<div class="zodiac abs" style="left:574px">
  <div class="sign-icon" role="img" aria-label="Leo sign"><svg viewBox="0 0 44 44"><circle cx="17" cy="25" r="4"/><path d="M20 22Q18 14 24 13Q30 13 28 21Q26 27 30 31Q32 32 33 30"/></svg></div>
  <span>LEO</span>
</div>

<section class="reading abs"></section>
<svg class="abs" style="left:412px;top:882px" width="14" height="8" viewBox="0 0 14 8"><path d="M0 0h14L7 8z" fill="#1b1b1b"/></svg>
<div class="tab abs" style="left:68px">YESTERDAY</div>
<div class="tab current abs" style="left:158px">TODAY</div>
<svg class="abs" style="left:192px;top:925px" width="10" height="6" viewBox="0 0 10 6"><path d="M0 0h10L5 6z" fill="#8a1a8a"/></svg>
<div class="tab abs" style="left:247px">TOMORROW</div>
<div class="reading-date abs">SUNDAY 08/02/2015</div>
<p class="reading-text abs">Lorem ipsum dolor sit amet, consectetuer adipiscing elit, sed diam nonummy nibh euismod tincidunt ut laoreet dolore magna aliquam erat volutpat.<br>Duis autem vel eum iriure dolor in hendrerit in vulputate velit esse molestie consequat, vel illum dolore eu feugiat nulla facilisis at vero eros et accumsan et iusto odio dignissim qui blandit praesent luptatum zzril delenit augue duis dolore te feugait nulla facilisi. Nam liber tempor cum soluta nobis eleifend option congue nihil imperdiet doming id quod mazim placerat facer possim assum.</p>

<aside class="stats abs">
  <h4>RATING</h4>
  <svg class="stars" width="54" height="10" viewBox="0 0 54 10">
    <g fill="#f08a00">
      <polygon points="5,0 6.2,3.6 10,3.6 7,5.9 8.1,9.6 5,7.3 1.9,9.6 3,5.9 0,3.6 3.8,3.6"/>
      <polygon transform="translate(11 0)" points="5,0 6.2,3.6 10,3.6 7,5.9 8.1,9.6 5,7.3 1.9,9.6 3,5.9 0,3.6 3.8,3.6"/>
      <polygon transform="translate(22 0)" points="5,0 6.2,3.6 10,3.6 7,5.9 8.1,9.6 5,7.3 1.9,9.6 3,5.9 0,3.6 3.8,3.6"/>
      <polygon transform="translate(33 0)" points="5,0 6.2,3.6 10,3.6 7,5.9 8.1,9.6 5,7.3 1.9,9.6 3,5.9 0,3.6 3.8,3.6"/>
    </g>
    <polygon transform="translate(44 0)" points="5,0 6.2,3.6 10,3.6 7,5.9 8.1,9.6 5,7.3 1.9,9.6 3,5.9 0,3.6 3.8,3.6" fill="none" stroke="#f08a00" stroke-width=".9"/>
    <path transform="translate(44 0)" d="M5 0L3.8 3.6H0l3 2.3-1.1 3.7L5 7.3z" fill="#f08a00"/>
  </svg>
  <h4>INTENSITY</h4><p>Lorem ipsum dolor sit amet</p>
  <h4>KEY WORDS</h4><p>Duis autem vel eum</p>
  <h4>MOOD</h4><p>Claritas est etiam processus</p>
</aside>

<footer class="site-footer abs"></footer>
<h3 class="footer-title abs" style="left:68px">OUR BLOG</h3>
<div class="post-thumb abs" style="top:1074px" role="img" aria-label="Blog image of a blue zodiac wheel"></div>
<div class="post-title abs" style="top:1073px">Lorem ipsum dolor sit</div>
<p class="post-excerpt abs" style="top:1086px">Ut wisi enim ad minim veniam, quis nostrud...</p>
<div class="post-thumb abs" style="top:1121px;background:linear-gradient(135deg,#1a3a8a,#c02a3a 50%,#2a4a9a)" role="img" aria-label="Blog image of a red and blue zodiac chart"></div>
<div class="post-title abs" style="top:1120px">Lorem ipsum dolor sit</div>
<p class="post-excerpt abs" style="top:1133px">Ut wisi enim ad minim veniam, quis nostrud...</p>

<h3 class="footer-title abs" style="left:245px">QUICK LINKS</h3>
<ul class="quick-links abs" style="left:246px;top:1071px">
  <li>Home</li><li>About Us</li><li>Our Service</li><li>FAQ</li><li>Contact Us</li>
</ul>
<ul class="quick-links abs" style="left:314px;top:1071px">
  <li>Testimonials</li><li>Privacy Policy</li><li>Sitemap</li><li>Terms &amp; Conditions</li>
</ul>

<h3 class="footer-title abs" style="left:422px">CONNECT US</h3>
<ul class="social abs">
  <li><i style="background:#3b5a9a"></i>Chatterly</li>
  <li><i style="background:#2aa3d8"></i>Chirpnest</li>
  <li><i style="background:#1a6aa0"></i>WorkWeave</li>
  <li><i style="background:#d2412e"></i>Orbitly</li>
  <li><i style="background:#e8701a"></i>RSS</li>
</ul>

<h3 class="footer-title abs" style="left:529px">NEWSLETTER</h3>
<div class="field abs" style="top:1070px">Name</div>
<div class="field abs" style="top:1099px">Email Address</div>
<div class="subscribe abs">SUBSCRIBE</div>

<div class="footer-base abs">Copyrights @ 2015 Starlit Astrology. All Right Reserved.</div>

</body>
</html>
```